Cover for a short novel to be published as an e-book.

I'm looking for an image to use for my e-book cover. It's a short (~42k words) novel/novella that deals humorously with the afterlife and some religious/mythological themes.

I was thinking something that was more graphic design-based rather than illustrative, and it would be awesome if it could somehow convey that it's a light, humorous story.

I plan to self-publish, so the image will end up being fairly small, but it should have some pop to draw people in.

Here's the text for the cover:

A Quiet Hour Before Supper
a novel(la) by Colin Brasby

```html
<!DOCTYPE html>
<html lang="en">
<head>
<meta charset="utf-8">
<title>A Quiet Hour Before Supper — Cover</title>
<link rel="stylesheet" href="https://fonts.googleapis.com/css2?family=Cinzel:wght@400;500&family=Archivo+Black&display=swap">
<style>
  :root {
    --page-bg: #e9e9eb;
    --cover-bg: #ffffff;
    --band: #2e2f3a;
    --band-text: #f2f2f4;
    --ink: #141416;
    --ink-slate: #3a3b46;
    --title-red: #b3141b;
    --mark-red: #e3161c;
    --suit-dark: #23252b;
    --suit-mid: #3e4149;
  }
  * { margin: 0; padding: 0; box-sizing: border-box; }
  html, body {
    width: 1200px; height: 900px; overflow: hidden;
    background: var(--page-bg);
  }
  .canvas {
    position: relative; width: 1200px; height: 900px;
    display: flex; justify-content: center;
  }
  .cover {
    position: relative; width: 640px; height: 900px;
    background: var(--cover-bg);
    overflow: hidden;
    box-shadow: 0 0 24px rgba(0,0,0,0.12);
  }
  .byline-band {
    position: absolute; top: 0; left: 0; right: 0; height: 108px;
    background: var(--band);
    color: var(--band-text);
    font-family: "Cinzel", serif;
    text-align: center;
    display: flex; flex-direction: column; justify-content: center;
    line-height: 1.12;
  }
  .byline-band .label { font-size: 28px; letter-spacing: 1px; }
  .byline-band .author { font-size: 31px; letter-spacing: 1px; }
  .title {
    position: absolute; top: 128px; left: 0; right: 0;
    font-family: "Cinzel", serif;
    text-align: center;
    font-weight: 400;
  }
  .title span { display: block; line-height: 1; }
  .title .line-small { font-size: 62px; color: var(--ink); }
  .title .line-big { font-size: 118px; color: var(--ink-slate); margin-top: -2px; }
  .title .line-mid { font-size: 62px; color: var(--ink); margin-top: -4px; }
  .title .line-red { font-size: 86px; color: var(--title-red); margin-top: -2px; }
  .question-mark {
    position: absolute; top: 430px; left: 0; right: 0;
    text-align: center;
    font-family: "Archivo Black", sans-serif;
    font-size: 250px; line-height: 1;
    color: var(--mark-red);
  }
  .suit-figure {
    position: absolute; left: 62px; bottom: 0; width: 520px; height: 212px;
    border-radius: 150px 150px 0 0 / 70px 70px 0 0;
    background: linear-gradient(180deg, var(--suit-mid) 0%, var(--suit-dark) 100%);
  }
</style>
</head>
<body>
  <main class="canvas">
    <section class="cover">
      <header class="byline-band">
        <span class="label">A Novel By</span>
        <span class="author">Colin Brasby</span>
      </header>
      <h1 class="title">
        <span class="line-small">The Quiet</span>
        <span class="line-big">Hour</span>
        <span class="line-mid">Before</span>
        <span class="line-red">Supper</span>
      </h1>
      <div class="question-mark" aria-hidden="true">?</div>
      <div class="suit-figure" role="img" aria-label="Photo of a headless figure in a dark suit, white shirt and black tie"></div>
    </section>
  </main>
</body>
</html>
```